Postcard design for Intellectual Property Professional Conference

Seeking design for 5.5" by 8.5" postcard mailer about a conference on tax and finance issues for international IP management. Attendees are lawyers and financial executives. Draft language is attached.

Target Market(s)

The project should have the attached picture of Boston with the caption "Courtesy of the Harborline Meetings & Travelers Council"

Industry/Entity Type

Finance

```html
<!DOCTYPE html>
<html lang="en">
<head>
<meta charset="utf-8">
<title>Increasing Profits &amp; Protecting Intellectual Property in Developing Growth Markets</title>
<link rel="stylesheet" href="https://fonts.googleapis.com/css2?family=Oswald:wght@400;500&family=PT+Sans:wght@400;700&display=swap">
<style>
  :root {
    --backdrop: #646567;
    --card: #ffffff;
    --navy: #0f3b5e;
    --red: #d9262c;
    --sky-top: #7fb8f0;
    --sky-mid: #a9cfee;
    --harbor: #8a6a55;
    --badge-blue: #1ba3e6;
    --body-text: #2b2b2b;
    --link-blue: #1ba3e6;
  }
  * { margin: 0; padding: 0; box-sizing: border-box; }
  html, body {
    width: 801px; height: 1200px; overflow: hidden;
    background: var(--backdrop);
  }
  .postcard {
    position: absolute; left: 52px; top: 57px;
    width: 698px; height: 1078px;
    background: var(--card); overflow: hidden;
  }
  .artwork { position: absolute; left: 0; top: 0; }
  .headline {
    position: absolute; left: 43px; top: 46px; width: 620px;
    font-family: "Oswald", sans-serif; font-weight: 500;
    font-size: 35px; line-height: 48px; letter-spacing: -0.6px;
    color: var(--navy); text-transform: uppercase;
  }
  .event-meta {
    position: absolute; left: 44px; top: 202px;
    font-family: "Oswald", sans-serif; font-weight: 500;
    font-size: 19px; line-height: 24px; letter-spacing: -0.2px;
    color: var(--red); text-transform: uppercase;
  }
  .register-badge {
    position: absolute; left: 438px; top: 344px; width: 188px;
    font-family: "Oswald", sans-serif; font-weight: 500;
    font-size: 27px; line-height: 36px; letter-spacing: -0.5px;
    color: #fff; text-align: center; text-transform: uppercase;
  }
  .intro {
    position: absolute; left: 43px; top: 592px; width: 262px;
    font-family: "PT Sans", sans-serif; font-size: 14px; line-height: 18px;
    color: var(--body-text);
  }
  .intro p + p { margin-top: 18px; }
  .website {
    position: absolute; left: 43px; top: 1012px;
    font-family: "PT Sans", sans-serif; font-weight: 700; font-size: 19px;
    color: var(--link-blue); text-decoration: none;
  }
  .topics {
    position: absolute; left: 350px; top: 584px; width: 325px;
    font-family: "PT Sans", sans-serif; color: var(--body-text);
  }
  .topics h2 {
    font-size: 17px; font-weight: 700; letter-spacing: 1.2px;
    color: var(--red); margin-bottom: 8px;
  }
  .topics ul { list-style: none; }
  .topics li {
    position: relative; padding-left: 15px;
    font-size: 14px; line-height: 18px; margin-bottom: 7px;
  }
  .topics li::before {
    content: ""; position: absolute; left: 0; top: 5px;
    border-left: 7px solid var(--red);
    border-top: 4.5px solid transparent; border-bottom: 4.5px solid transparent;
  }
</style>
</head>
<body>
<main class="postcard">
  <svg class="artwork" width="698" height="1078" viewBox="0 0 698 1078">
    <defs>
      <linearGradient id="harbor-photo" x1="0" y1="0" x2="0" y2="1">
        <stop offset="0" stop-color="var(--sky-top)"/>
        <stop offset="0.4" stop-color="var(--sky-mid)"/>
        <stop offset="0.7" stop-color="#b98a6e"/>
        <stop offset="1" stop-color="var(--harbor)"/>
      </linearGradient>
    </defs>
    <rect class="city-photo" x="0" y="0" width="698" height="600" fill="url(#harbor-photo)"
          role="img" aria-label="Boston waterfront skyline with towers and a bridge over the harbor"/>
    <polygon class="lower-panel" fill="var(--card)"
             points="0,533 48,496 143,558 300,490 448,538 668,123 698,123 698,1078 0,1078"/>
    <polyline class="growth-arrow" fill="none" stroke="var(--red)" stroke-width="17" stroke-linejoin="miter"
              points="-5,537 48,496 143,558 300,490 448,538 660,140"/>
    <polygon class="growth-arrow-head" fill="var(--red)" points="632,110 700,86 690,165"/>
    <circle class="register-circle" cx="532" cy="413" r="93" fill="var(--badge-blue)"/>
  </svg>

  <h1 class="headline">Increasing Profits &amp; Protecting Intellectual Property in Developing Growth Markets</h1>
  <p class="event-meta">Boston<br>March 24 &amp; 25, 2016</p>
  <p class="register-badge">Register<br>Early<br>and save up<br>to $300</p>

  <section class="intro">
    <p>You are cordially invited to attend a comprehensive and practical day and a half conference to examine the tax and legal structuring strategies for increasing profits from Intellectual properties while protecting these important assets when doing business in fast growing developing markets. Intellectual property assets include some of the most important assets of most companies: their patents, trade marks, copyrights, brand names and licensing agreements.</p>
    <p>Senior tax, legal and financial experts will provide a comprehensive analysis of the legal issues, recent tax &amp; regulatory developments, skills and structuring strategies necessary to maximize profits from IP Migrating IP assets to low tax jurisdiction will also be covered along with dealing with issues of piracy, counterfeiting, infringement and other legal challenges to a company's IP.</p>
  </section>
  <a class="website" href="#">www.ipgrowthforum.com</a>

  <section class="topics">
    <h2>TOPICS TO BE COVERED INCLUDE:</h2>
    <ul>
      <li>Market trends in IP tax &amp; legal structures</li>
      <li>Proposed US Tax changes and regulatory developments outside the US including European and OECD developments affecting IP, patent box, base erosion and profit splitting (BEPS)</li>
      <li>Overview of the IP landscape in key developing growth markets such as China, India, Brazil, Korea, South Africa, Mexico and other developing markets outside the US.</li>
      <li>Legal issues including litigation, arbitration and use of government assistance to protect IP values in key developing markets.</li>
      <li>Monetizing IP assets and rights in regard to divestitures, spin offs, split offs, M&amp;A, transfers of ownership and securitizations in developing growth markets</li>
      <li>Special Tax Planning and Legal Considerations for IP in Particular Sectors such as Biopharmaceutical, International Sports Licensing, High Tech, Consumer Brands, and Manufacturing</li>
      <li>Restructuring and Migration of IP Assets to Tax Advantaged Jurisdictions</li>
    </ul>
  </section>
</main>
</body>
</html>
```